VelmaRin packaging label

I would like to have designs for a range of packaging labels for an 100% organic skincare and cosmetics product range. The designer will first need to visit the following website and choose a packaging bottle or jar first and then design a "sticker" label which can stick onto the bottle or jars. I have attached the logo. The product is a luxury skincare product which focuses on 100% organic ingredients and putting the true glow back into people's skin.
http://shop.kestrelvane.example.au/epages/kestrelvane.sf/en_AU/?ObjectPath=/Shops/kestrelvane/Categories/16
The bottles and jars will be for 50ml and 100ml. I prefer the amber glass bottles for cleansers, toners and jars for moisturisers. Labels may include designs which can be sticked around the jar or bottles and onto the cap of the jar.
I particularly like "vintage designs" as it reflects the "luxury" status of the products. I also like "organic" designs. Please ensure the design sets my products apart from the rest and is eye catching when placed with other products on the shelfs.
I have attached some packaging samples which I really like. The sticker can be custom cut, rectangular, circle, oval in shape etc.
Please make the design editable (send me ai as well as editable pdf) so that I can put the names of the products eg toner, cleaner on it. You may choose to design a range of labels or 1-2 which can be used on every product.
Target Market(s)
High income working class and rich house wives.
Requirements
Must have
- Elegance
Please also use the similar design but for different sizes and products.
1. sticker labels for amber glass 50ml jar. For jar and round cap.
2. Sticker labels for 15 ml serum
3. 100 ml for amber glass toner and cleanser bottles.
Nice to have
- Eye catchy

```html
<!DOCTYPE html>
<html lang="en">
<head>
<meta charset="utf-8">
<title>VelmaRin packaging labels</title>
<link rel="stylesheet" href="https://fonts.googleapis.com/css2?family=Questrial&family=Arimo:wght@400&display=swap">
<style>
  :root {
    --bg-light: #f4f4f4;
    --bg-dark: #d6d6d6;
    --label-rose: #d8b8aa;
    --label-rose-soft: #dcbdb0;
    --lattice: #c9a594;
    --brown: #6a3d1e;
    --cream: #f2e3d9;
    --ink: #5a3419;
  }
  * { box-sizing: border-box; margin: 0; padding: 0; }
  html, body { width: 1200px; height: 1000px; overflow: hidden; }
  body {
    position: relative;
    background: linear-gradient(90deg, var(--bg-light) 0%, #ececec 60%, var(--bg-dark) 100%);
    font-family: "Questrial", "Century Gothic", sans-serif;
    color: var(--cream);
  }
  .label {
    position: absolute;
    background: var(--label-rose);
    overflow: hidden;
  }
  .lattice {
    position: absolute; inset: 0;
    background: linear-gradient(135deg, var(--label-rose-soft), var(--lattice) 50%, var(--label-rose-soft));
    opacity: .55;
  }
  .badge { position: absolute; }
  .badge svg { position: absolute; inset: 0; width: 100%; height: 100%; }
  .badge-content {
    position: absolute; inset: 0;
    display: flex; flex-direction: column; align-items: center;
    text-align: center;
  }
  .brand-dot {
    border-radius: 50%;
    background: var(--cream);
  }
  .brand {
    text-transform: uppercase;
    letter-spacing: .08em;
    color: var(--cream);
  }
  .product { color: var(--cream); }
  .claim {
    background: var(--label-rose);
    color: var(--ink);
    border: 1px solid var(--cream);
    border-radius: 6px;
    white-space: nowrap;
  }
  .volume { color: var(--cream); }

  /* jar label */
  .jar-label { left: 80px; top: 380px; width: 465px; height: 312px; }
  .jar-label .badge { left: 82px; top: 44px; width: 300px; height: 264px; }
  .jar-label .brand-dot { width: 30px; height: 30px; margin-top: 28px; }
  .jar-label .brand { font-size: 22px; margin-top: 14px; }
  .jar-label .product { font-size: 16px; margin-top: 22px; }
  .jar-label .claim { font-size: 12.5px; padding: 2px 8px; margin-top: 6px; }
  .jar-label .volume { font-size: 11px; margin-top: 44px; }

  /* serum label */
  .serum-label { left: 560px; top: 520px; width: 147px; height: 146px; }
  .serum-label .badge { left: 18px; top: 20px; width: 111px; height: 108px; }
  .serum-label .brand-dot { width: 12px; height: 12px; margin-top: 12px; }
  .serum-label .brand { font-size: 9px; margin-top: 5px; }
  .serum-label .product { font-size: 6.5px; margin-top: 12px; }
  .serum-label .claim { font-size: 5px; padding: 1px 3px; margin-top: 3px; border-radius: 3px; }
  .serum-label .volume { font-size: 4.5px; margin-top: 17px; }

  /* wrap label, laid out flat then turned upright */
  .wrap-label { left: 824px; top: 42px; width: 300px; height: 913px; }
  .wrap-inner {
    position: absolute;
    width: 913px; height: 300px;
    left: 0; top: 913px;
    transform-origin: 0 0;
    transform: rotate(-90deg);
  }
  .wrap-inner .badge { left: 30px; top: 14px; width: 360px; height: 272px; }
  .wrap-inner .brand-dot { width: 30px; height: 30px; margin-top: 40px; }
  .wrap-inner .brand { font-size: 22px; margin-top: 14px; }
  .wrap-inner .product { font-size: 16px; margin-top: 10px; }
  .wrap-inner .claim { font-size: 12.5px; padding: 2px 8px; margin-top: 5px; }
  .wrap-inner .volume { font-size: 11px; margin-top: 30px; }

  .info-panel {
    position: absolute;
    left: 475px; top: 12px; width: 418px; height: 278px;
    background: var(--label-rose-soft);
    border: 1px solid var(--brown);
    border-radius: 14px;
    padding: 16px 12px 10px 14px;
    color: var(--ink);
    font-family: "Arimo", Arial, sans-serif;
    font-size: 9.3px;
    line-height: 11.4px;
    display: flex; flex-direction: column;
  }
  .info-tag {
    align-self: flex-start;
    margin-left: 180px;
    background: var(--brown);
    color: var(--cream);
    border: 1px solid var(--cream);
    border-radius: 3px;
    padding: 1px 6px;
    font-family: "Questrial", sans-serif;
    font-size: 8px;
  }
  .info-copy { margin-top: 8px; }
  .info-copy p + p { margin-top: 8px; }
  .info-footer {
    margin-top: auto;
    display: flex; align-items: flex-end;
  }
  .info-address { font-size: 7.5px; line-height: 10px; width: 190px; }
  .info-brand {
    display: flex; flex-direction: column; align-items: center;
    color: var(--ink);
  }
  .info-brand .brand-dot { width: 14px; height: 14px; background: var(--brown); }
  .info-brand .brand { color: var(--ink); font-size: 11px; margin-top: 6px; }
</style>
</head>
<body>

<section class="label jar-label" aria-label="Hand and body lotion jar label">
  <div class="lattice" role="img" aria-label="Vintage lattice pattern in rose and brown"></div>
  <div class="badge">
    <svg viewBox="0 0 300 264" preserveAspectRatio="none" aria-hidden="true">
      <path d="M38,4 H262 A34,34 0 0 0 296,38 V226 A34,34 0 0 0 262,260 H38 A34,34 0 0 0 4,226 V38 A34,34 0 0 0 38,4 Z" fill="var(--brown)"/>
      <path d="M42,12 H258 A30,30 0 0 0 288,42 V222 A30,30 0 0 0 258,252 H42 A30,30 0 0 0 12,222 V42 A30,30 0 0 0 42,12 Z" fill="none" stroke="var(--cream)" stroke-width="2"/>
    </svg>
    <div class="badge-content">
      <span class="brand-dot"></span>
      <span class="brand">VelmaRin</span>
      <span class="product">hand and body lotion</span>
      <span class="claim">100% organic skin care</span>
      <span class="volume">50 ml</span>
    </div>
  </div>
</section>

<section class="label serum-label" aria-label="Brightening serum bottle label">
  <div class="lattice" role="img" aria-label="Vintage lattice pattern in rose and brown"></div>
  <div class="badge">
    <svg viewBox="0 0 300 264" preserveAspectRatio="none" aria-hidden="true">
      <path d="M38,4 H262 A34,34 0 0 0 296,38 V226 A34,34 0 0 0 262,260 H38 A34,34 0 0 0 4,226 V38 A34,34 0 0 0 38,4 Z" fill="var(--brown)"/>
      <path d="M44,14 H256 A30,30 0 0 0 286,44 V220 A30,30 0 0 0 256,250 H44 A30,30 0 0 0 14,220 V44 A30,30 0 0 0 44,14 Z" fill="none" stroke="var(--cream)" stroke-width="4"/>
    </svg>
    <div class="badge-content">
      <span class="brand-dot"></span>
      <span class="brand">VelmaRin</span>
      <span class="product">brightening serum</span>
      <span class="claim">100% organic skin care</span>
      <span class="volume">15 ml</span>
    </div>
  </div>
</section>

<section class="label wrap-label" aria-label="Wrap-around jar label, flat">
  <div class="lattice" role="img" aria-label="Vintage lattice pattern in rose and brown"></div>
  <div class="wrap-inner">
    <div class="badge">
      <svg viewBox="0 0 300 264" preserveAspectRatio="none" aria-hidden="true">
        <path d="M38,4 H262 A34,34 0 0 0 296,38 V226 A34,34 0 0 0 262,260 H38 A34,34 0 0 0 4,226 V38 A34,34 0 0 0 38,4 Z" fill="var(--brown)"/>
        <path d="M42,12 H258 A30,30 0 0 0 288,42 V222 A30,30 0 0 0 258,252 H42 A30,30 0 0 0 12,222 V42 A30,30 0 0 0 42,12 Z" fill="none" stroke="var(--cream)" stroke-width="2"/>
      </svg>
      <div class="badge-content">
        <span class="brand-dot"></span>
        <span class="brand">VelmaRin</span>
        <span class="product">hand and body lotion</span>
        <span class="claim">100% organic skin care</span>
        <span class="volume">50 ml</span>
      </div>
    </div>

    <div class="info-panel">
      <span class="info-tag">hand and body lotion</span>
      <div class="info-copy">
        <p>Lorem ipsum dolor sit amet, consectetur adipisicing elit, sed do eiusmod pro empor incididunt ut labore et dolore magna aliqua. Ut enim ad minim pore eniam, quis nostrud exercitation ullamco laboris nisi ut aliquip ex ea ommodo consequat. Duis aute irure dolor in reprehenderit in voluptate velit esse cillum dolore eu fugiat nulla pariatur.</p>
        <p>DIRECTIONS: Quis nostrud exercitation ullamco laboris nisi ut aliquip ex ea commodo consequat. Duis aute irure dolor in reprehenderit in voluptate velit esse cillum dolore eu fugiat nulla pariatur. Excepteur sint occaecat cupidata.</p>
        <p>INGREDIENTS: Non proident, Sunt in culpa qui. Officia deserunt mollit anim id est laborum.</p>
      </div>
      <div class="info-footer">
        <div class="info-address">No Street Name, City Name<br>State Name Zip Code<br>1-800-0000<br>www.website.com</div>
        <div class="info-brand">
          <span class="brand-dot"></span>
          <span class="brand">VelmaRin</span>
        </div>
      </div>
    </div>
  </div>
</section>

</body>
</html>
```